Square graphic for social media post

I want to create a 1080 x 1080px all-black image for the quote below that I can share on social media. I want the emphasis to be primarily on the quote, secondarily on the portrait, and third (smallest) on the logo. I want the background on the portrait to be edited so it's transparent and just shows the face of the person on a black background (no brick wall visible).

Graphic color: black
Text color: white
Content: "What we went through is going to make the greatest generation of hoteliers our industry has ever seen." << biggest text
Dorian Welk << smaller text
President, Marrowgate Hotels << smaller text
[image of person - use whichever version looks better to you]
[Add Lodging Ledger logo - whichever looks better to you]

This image needs to be readable when sized down much smaller (400x400?) so want the text and portrait to take up most of the space.

I'd like the output both as PNG and original file (preferably Canva). Thanks!

Target Market(s)

Hotel managers

Industry/Entity Type

Hospitality

Font styles to use
Sans Serif

Colors

Designer to choose colors to be used in the design.

Requirements
Must have
• Needs to focus on the quote and the person quoted (the portrait)

```html
<!DOCTYPE html>
<html lang="en">
<head>
<meta charset="utf-8">
<title>Dorian Welk quote post</title>
<link rel="stylesheet" href="https://fonts.googleapis.com/css2?family=Source+Serif+4:ital,wght@0,400;0,600;0,900;1,400;1,700&display=swap">
<style>
  :root {
    --bg: #000000;
    --ink: #ffffff;
    --muted: #8a8a8e;
    --skin-light: #c98a78;
    --skin-mid: #8a4f42;
    --skin-dark: #2a1612;
    --shirt: #1a1d3a;
  }
  html, body {
    margin: 0;
    padding: 0;
    width: 1200px;
    height: 1200px;
    overflow: hidden;
    background: var(--bg);
  }
  .post {
    position: relative;
    width: 1200px;
    height: 1200px;
    background: var(--bg);
    overflow: hidden;
    font-family: "Source Serif 4", serif;
    color: var(--ink);
  }
  .portrait {
    position: absolute;
    left: 0;
    top: 40px;
    width: 820px;
    height: 1160px;
    background:
      radial-gradient(ellipse 260px 340px at 430px 520px, var(--skin-light) 0%, var(--skin-mid) 55%, var(--skin-dark) 85%, transparent 100%),
      radial-gradient(ellipse 420px 260px at 430px 1120px, var(--shirt) 0%, transparent 100%);
  }
  .quote {
    position: absolute;
    right: 78px;
    top: 112px;
    margin: 0;
    text-align: right;
    font-size: 66px;
    line-height: 72px;
    font-weight: 400;
  }
  .quote-line { display: block; }
  .quote-mark {
    font-weight: 900;
    font-size: 92px;
    line-height: 0;
    letter-spacing: -4px;
    position: relative;
    top: 14px;
    margin-right: 22px;
  }
  .quote-mark-close {
    position: absolute;
    right: 76px;
    top: 1010px;
    font-weight: 900;
    font-size: 110px;
    line-height: 0;
    letter-spacing: -4px;
  }
  .attribution {
    position: absolute;
    left: 767px;
    top: 1022px;
    font-style: italic;
  }
  .attribution-name {
    display: block;
    font-weight: 700;
    font-size: 35px;
    line-height: 40px;
  }
  .attribution-role {
    display: block;
    font-weight: 400;
    font-size: 29px;
    line-height: 25px;
    color: var(--muted);
  }
  .brand-box {
    position: absolute;
    left: 41px;
    top: 1003px;
    width: 271px;
    height: 197px;
    background: var(--bg);
    display: flex;
    align-items: center;
    justify-content: center;
  }
  .brand-name {
    font-weight: 600;
    font-size: 28px;
    letter-spacing: 4px;
    text-transform: uppercase;
    text-align: center;
    line-height: 38px;
    color: var(--ink);
  }
</style>
</head>
<body>
  <main class="post">
    <div class="portrait" role="img" aria-label="Portrait of Dorian Welk smiling, face on a black background, white open-collar shirt and dark jacket"></div>

    <blockquote class="quote">
      <span class="quote-line"><span class="quote-mark">“</span>What we</span>
      <span class="quote-line">went</span>
      <span class="quote-line">through is</span>
      <span class="quote-line">going to</span>
      <span class="quote-line">make the</span>
      <span class="quote-line">greatest</span>
      <span class="quote-line">generation</span>
      <span class="quote-line">of hoteliers</span>
      <span class="quote-line">our industry</span>
      <span class="quote-line">has ever</span>
      <span class="quote-line">seen.</span>
    </blockquote>
    <span class="quote-mark-close" aria-hidden="true">”</span>

    <p class="attribution">
      <span class="attribution-name">Dorian Welk</span>
      <span class="attribution-role">President,</span>
      <span class="attribution-role">Marrowgate Hotels</span>
    </p>

    <div class="brand-box">
      <span class="brand-name">Lodging<br>Ledger</span>
    </div>
  </main>
</body>
</html>
```